Website Design for Marwen Ridge Estates

I need the attached Adobe Illustrator/pdf files made into website pages. The brochure currently is a bifold with pages 4,1 and 2,3 left to right, top to bottom .I would like to see the pages on the site placed as pg2 first followed by 3,4,1. Links need to be live.
A contact button would be great instead of using the gmail address and could link to a contact page from another website (https://www.brightcoveptdc.com/contact-us) that I currently have. I wouldn't mind driving people to that site too or have a protected contact page to keep spam away as much as possible. Photos need to be easy to change out and text and photos on the current page 4 need to be easy to update.
I own the domain, marwenridgeestates.com through Namebarn and can give access to set up the site through them or am willing to go with what ever route would be the least expensive.
I do not understand how to make a website nor understand what coding and Wordpress are so will need someone very patient. I do check my email several times a day and will try to get questions answered within 24 hours. I am including extra photos, logos etc
Here is a link to access some photos to start with: https://bcpdc-my.filehubnet.com/:f:/p/margaret/Kq4TnW82pLdYv7RbxoNcJsAe1fGz9hUkMmQwePtrZzxBvC?e=Hx3Lpo

Target Market(s)

Real Estate buyers

Industry/Entity Type

real estate for sale

Coding

Coded - Design and coding required

Number of Pages Required

3 page

Font styles to use
Other font styles liked:
• century gothic

Requirements
Must have
• read explaination above, contact page, links to various contacts, photos albums, possible ability to play video, be able to work on myself or simple way to contact designer to do changes in the future.
Nice to have
• visual beauty with photos, use colors of logo, link to print pdf of brochure.

```html
<!DOCTYPE html>
<html lang="en">
<head>
<meta charset="utf-8">
<title>Marwen Ridge Estates</title>
<link href="https://fonts.googleapis.com/css2?family=Questrial&display=swap" rel="stylesheet">
<style>
:root{
  --red:#ac2c3b;
  --yellow:#fcae10;
  --white:#ffffff;
  --off:#f5f5f5;
  --stage:#f5e7eb;
  --ink:#4a4a4a;
  --muted:#7a7a7a;
}
*{box-sizing:border-box;margin:0;padding:0}
html,body{width:1200px;height:3735px;overflow:hidden}
body{background:var(--stage);font-family:"Questrial",sans-serif;color:var(--ink)}
.page{position:absolute;left:196px;top:33px;width:808px;height:3669px;background:var(--white);overflow:hidden;box-shadow:0 2px 14px rgba(0,0,0,.08)}
.abs{position:absolute}
.topbar{left:0;top:0;width:808px;height:17px;background:var(--red);color:#fff;font-size:7px;display:flex;justify-content:flex-end;align-items:center;gap:18px;padding-right:26px}
.topbar svg{vertical-align:middle;margin-right:3px}
.nav{left:0;top:17px;width:808px;height:69px;display:flex;align-items:center;padding:0 158px}
.brand{display:flex;align-items:center;gap:6px;color:var(--red);font-size:9px}
.brand-mark{width:28px;height:28px;border-radius:50%;background:var(--yellow)}
.menu{margin-left:auto;display:flex;align-items:center;gap:22px;font-size:8px;color:var(--muted)}
.btn{background:var(--yellow);color:#fff;font-size:7px;padding:8px 14px;text-decoration:none}
.hero{left:0;top:86px;width:808px;height:454px;background:linear-gradient(180deg,#5d7fb8 0%,#9ab3d6 35%,#b59a6e 55%,#6e5a48 80%,#8a7d6e 100%)}
.hero h1{position:absolute;top:160px;width:100%;text-align:center;color:#fff;font-weight:400;font-size:28px;letter-spacing:1px}
.video{position:absolute;top:204px;left:0;width:100%;text-align:center;color:#fff;font-size:7px}
.play{display:block;margin:6px auto 0;width:44px;height:44px}
.banner{left:158px;top:492px;width:650px;height:93px;background:var(--red);color:var(--yellow);font-size:11px;display:flex;align-items:center;justify-content:center}
.photo{background:linear-gradient(160deg,#7e9cc8,#b39a72 55%,#5e4c3e)}
.photo-warm{background:linear-gradient(170deg,#9fb1c9,#c9a56e 45%,#8c6d4d)}
.tag{left:158px;top:795px;width:84px;height:82px;background:var(--yellow);color:#fff;font-size:9px;text-align:center;display:flex;align-items:center;justify-content:center;line-height:1.2}
.vert{left:178px;top:690px;transform:rotate(-90deg);transform-origin:left top;color:var(--red);font-size:6px;opacity:.6}
.belief h2{font-weight:400;font-size:12px;line-height:1.45;margin-bottom:10px}
.belief ul{list-style:none;font-size:5.6px;line-height:1.75}
.belief li::before{content:"• "}
.b1{left:452px;top:620px;width:200px}
.b1 h2{color:var(--red)}
.b2{left:158px;top:953px;width:246px;height:315px;background:var(--red);color:#fff;padding:36px 24px}
.b3{left:404px;top:1378px;width:245px;height:290px;background:var(--yellow);color:#fff;padding:36px 24px}
.gallery{left:0;top:1744px;width:808px}
.cottage{left:158px;top:2458px;width:492px}
.cottage h2{text-align:center;color:var(--red);font-weight:400;font-size:14px}
.lead{text-align:center;font-size:5.6px;line-height:1.7;color:var(--muted);margin-top:10px}
.col{position:absolute;font-size:5.6px;line-height:1.8;color:var(--muted)}
.col h3{color:var(--red);font-weight:400;font-size:6.5px;margin-bottom:8px}
.col ul{list-style:none}
.col li::before{content:"• "}
.plan{left:318px;top:2546px;width:162px;height:170px;background:linear-gradient(160deg,#eeeeee,#d9d9d9)}
.verified{left:0;top:2764px;width:808px;height:301px;background:linear-gradient(180deg,#b63a48,#a62a39);color:#fff;text-align:center}
.verified h2{margin-top:40px;font-weight:400;font-size:13px}
.verified p.sub{font-size:6.5px;margin-top:6px;opacity:.85}
.feat{position:absolute;width:150px;text-align:center}
.feat b{display:block;color:var(--yellow);font-weight:400;font-size:22px}
.feat span{font-size:6px}
.divider{position:absolute;width:1px;height:60px;background:rgba(255,255,255,.25)}
.more{left:158px;top:3125px;width:250px}
.more h2{color:var(--red);font-weight:400;font-size:14px;margin-bottom:14px}
.more ul{list-style:none;font-size:5.6px;line-height:1.8;color:var(--muted)}
.more li::before{content:"• "}
.home-img{left:423px;top:3103px;width:229px;height:200px;background:linear-gradient(170deg,#a9bcd4,#c8b48f 60%,#8b7a62)}
.price{left:465px;top:3285px;width:145px;height:40px;background:var(--red);color:#fff;text-align:center;font-size:11px;padding-top:6px}
.price small{display:block;font-size:5px;margin-top:2px}
.certs{left:0;top:3377px;width:808px;height:121px;background:var(--off);display:flex;justify-content:center;align-items:center;gap:42px}
.cert{display:flex;align-items:center;gap:6px;font-size:5.6px;color:var(--muted);line-height:1.5}
.cert i{width:26px;height:26px;border-radius:50%;background:#c9d6c3;display:block}
.footer{left:0;top:3498px;width:808px;height:171px;background:var(--yellow);color:#fff;text-align:center}
.footer .brand{justify-content:center;color:#fff;margin-top:48px;font-size:10px}
.footer .brand-mark{background:#fff;opacity:.85}
.footer p{font-size:6px;margin-top:14px;color:var(--red)}
</style>
</head>
<body>
<div class="page">
  <div class="abs topbar">
    <span><svg width="6" height="6" viewBox="0 0 10 10"><path d="M2 1l2 2-1 1.5a6 6 0 0 0 2.5 2.5L7 6l2 2-1.5 1.5C4 9 1 6 .5 2.5z" fill="#fcae10"/></svg>+1 (509)-555-0142 Opt 3</span>
    <span><svg width="7" height="5" viewBox="0 0 14 10"><rect width="14" height="10" fill="#fcae10"/><path d="M0 0l7 5 7-5" stroke="#ac2c3b" fill="none"/></svg>info@marwenridgeestates.com</span>
  </div>

  <header class="abs nav">
    <div class="brand"><span class="brand-mark"></span>Marwen Ridge Estates</div>
    <nav class="menu"><span>Home</span><span>About</span><span>Gallery</span><a class="btn" href="#contact">CONTACT US</a></nav>
  </header>

  <section class="abs hero" role="img" aria-label="Photo of a stucco home with a dark garage door under a blue sky">
    <h1>THE MARWEN RIDGE DIFFERENCE</h1>
    <div class="video">See Our Video
      <svg class="play" viewBox="0 0 44 44"><circle cx="22" cy="22" r="22" fill="#fcae10"/><path d="M18 14l12 8-12 8z" fill="#fff"/></svg>
    </div>
  </section>
  <div class="abs banner">For Sale By Builder (509)-555-0142 Opt 3 Call Today to Book a Tour!</div>

  <div class="abs photo" style="left:242px;top:619px;width:194px;height:258px" role="img" aria-label="Photo of a home exterior with garage"></div>
  <div class="abs tag">What<br>We<br>Believe</div>
  <div class="abs vert">Marwen Ridge Estates</div>
  <div class="abs belief b1">
    <h2>We believe everyone deserves to live in a healthy home free of toxins</h2>
    <ul>
      <li>Designed to meet Clean Air Standard</li>
      <li>Whole house air filtration, smooth, easy to clean surfaces and a tight building envelope keep smoke, pollen &amp; dust out and fresh filtered air in</li>
      <li>High efficiency air delivery</li>
      <li>Superior indoor air quality by using no or low toxin building materials</li>
      <li>Quiet premium drywall and insulation to minimize mechanical outside noise</li>
      <li>Bedrooms are wired to reduce magnetic fields</li>
      <li>PureFlow water treatment system</li>
      <li>Community open and gathering spaces and sidewalks</li>
    </ul>
  </div>

  <div class="abs photo-warm" style="left:385px;top:921px;width:264px;height:381px" role="img" aria-label="Photo of ornamental grasses beside a stone wall"></div>
  <div class="abs belief b2">
    <h2>We believe that no one wants to pay a power bill</h2>
    <ul>
      <li>Solar results lower and predictable energy bills</li>
      <li>Powered by the sun, each home is designed to be net zero and to produce as much power as it consumes</li>
      <li>Triple pane windows &amp; doors</li>
      <li>Designed to meet net zero standards</li>
      <li>Efficient appliance package and fixtures</li>
      <li>Superior insulation exceeding code standards by +30%</li>
      <li>Tight building envelope</li>
      <li>Mini split heating and cooling</li>
      <li>Large patio overhangs reduce overheating</li>
      <li>Heat pump water heater</li>
    </ul>
  </div>

  <div class="abs photo" style="left:158px;top:1346px;width:374px;height:354px" role="img" aria-label="Photo of a row of new homes with landscaping"></div>
  <div class="abs belief b3">
    <h2>We believe that we should build sustainably</h2>
    <ul>
      <li>Quality built, these homes are built to last 100 years by utilizing durable, sustainable and locally sourced materials and products</li>
      <li>Insulated concrete floors</li>
      <li>High quality building materials including stucco siding, metal roofing, trims and fixtures</li>
      <li>Highest grade materials are locally sourced</li>
      <li>Most of the waste from construction of these homes has been recycled</li>
      <li>Electric car charging ready</li>
    </ul>
  </div>

  <section class="abs gallery">
    <div class="abs" style="left:0;top:0;width:263px;height:330px;background:linear-gradient(180deg,#b6a999,#8d8073)" role="img" aria-label="Photo of a tiled walk-in shower"></div>
    <div class="abs photo-warm" style="left:269px;top:0;width:539px;height:330px" role="img" aria-label="Photo of a home with a covered wood patio"></div>
    <div class="abs" style="left:0;top:336px;width:538px;height:331px;background:linear-gradient(180deg,#6b5447,#dcdcdc 45%,#5d4a40)" role="img" aria-label="Photo of a kitchen with dark cabinets and steel appliances"></div>
    <div class="abs" style="left:544px;top:336px;width:264px;height:331px;background:linear-gradient(180deg,#d8d8d6,#9ea3aa 70%,#3f4856)" role="img" aria-label="Photo of an empty room with a window and polished floor"></div>
  </section>

  <section class="abs cottage">
    <h2>Larkin Cottage</h2>
    <p class="lead">Bright single level plan with open living, two bedrooms and a covered patio. Quality finishes throughout, built for healthy, efficient living with low monthly costs. Schedule a tour today and see the craftsmanship for yourself.</p>
  </section>
  <div class="col" style="left:158px;top:2560px;width:150px">
    <h3>Property Features</h3>
    <ul><li>Central Air &amp; Heating</li><li>Energy Efficient Systems</li><li>Water/Air Purification Systems</li><li>Smoke Free</li><li>2 Car Garage (Attached)</li><li>Bedrooms are wired to reduce magnetic fields</li><li>PureFlow water treatment system</li><li>Community open and gathering spaces and sidewalks</li></ul>
  </div>
  <div class="abs plan" role="img" aria-label="Floor plan drawings of the cottage"></div>
  <div class="col" style="left:505px;top:2560px;width:145px">
    <h3>Lot Features</h3>
    <ul><li>Lot Level</li><li>Lot Private</li><li>Garden View</li></ul>
    <h3 style="margin-top:32px">Additional Features</h3>
    <ul><li>Agent Commission Available</li></ul>
  </div>

  <section class="abs verified">
    <h2>All Marwen Ridge Homes Are Verified By a Third Party</h2>
    <p class="sub">And there's more...</p>
    <div class="feat" style="left:159px;top:110px"><b>01</b><span>Christmas Light Plug Ready</span></div>
    <div class="feat" style="left:327px;top:110px"><b>02</b><span>Smooth Wall Drywall</span></div>
    <div class="feat" style="left:493px;top:110px"><b>03</b><span>Commercial Grade Insulated Garage Door</span></div>
    <div class="feat" style="left:159px;top:219px"><b>04</b><span>Premium Grade Plumbing Fixtures</span></div>
    <div class="feat" style="left:327px;top:219px"><b>05</b><span>Premium Cabinet Package</span></div>
    <div class="feat" style="left:493px;top:219px"><b>06</b><span>Curbless Shower With Glass Rain Doors</span></div>
    <div class="divider" style="left:318px;top:105px"></div><div class="divider" style="left:485px;top:105px"></div>
    <div class="divider" style="left:318px;top:214px"></div><div class="divider" style="left:485px;top:214px"></div>
  </section>

  <section class="abs more">
    <h2>Even more to consider...</h2>
    <ul>
      <li>Designed to meet Clean Air Standard</li>
      <li>Whole house air filtration, smooth, easy to clean surfaces and a tight building envelope keep smoke, pollen &amp; dust out and fresh filtered air in</li>
      <li>High efficiency air delivery</li>
      <li>Superior indoor air quality by using no or low toxin building materials</li>
      <li>Quiet premium drywall and insulation to minimize mechanical outside noise</li>
      <li>Bedrooms are wired to reduce magnetic fields</li>
      <li>PureFlow water treatment system</li>
      <li>Community open and gathering spaces and sidewalks</li>
    </ul>
  </section>
  <div class="abs home-img" role="img" aria-label="Photo of the home framed in a house outline"></div>
  <div class="abs price">$399,500<small>802 Marwen Ridge Way, Alder, WA 98900</small></div>

  <section class="abs certs">
    <div class="cert"><i></i>Net-Zero Ready Certified<br>(zero energy ready)</div>
    <div class="cert"><i style="background:#c7d3e3"></i>Air Certified<br>(Clean Air Standard)</div>
    <div class="cert"><i style="background:#cfe0e6"></i>Water Saver Certified</div>
    <div class="cert"><i style="background:#d6dcb8"></i>Eco Build Verified<br>Gold<br>@ 2021</div>
  </section>

  <footer class="abs footer" id="contact">
    <div class="brand"><span class="brand-mark"></span>Marwen Ridge Estates</div>
    <p>+1 (509)-555-0142 Opt 3 &nbsp;&nbsp;&nbsp; info@marwenridgeestates.com</p>
  </footer>
</div>
</body>
</html>
```